tillstop Fountain Drink Program header Design

Designing a fountain drink machine graphics that attract to customers to buy the fountain drink. Along with the attractive price point on it. I am attaching my current program graphics on the machine but want to create something more attractive. Also want to incorporate our brand logo with it. Pay Less 79c is my current Design. tillstop is my convenience store brand name. The design theme should consist of ice cold fountain drink and price point of 79c for 32 oz. the fountain drink cups we have are white foam cups with tillstop logo on them. see attached as well

Target Market(s)

Thirsty Consumers

Industry/Entity Type

Convenience Store

Colors
acd136
fbed22
33a6d7

Requirements
Must have
• Ice Cold Drink theme

```html
<!DOCTYPE html>
<html lang="en">
<head>
<meta charset="utf-8">
<title>tillstop Fountain Drink Header</title>
<link rel="stylesheet" href="https://fonts.googleapis.com/css2?family=Luckiest+Guy&display=swap">
<style>
  :root {
    --sun-yellow: #fbed22;
    --pale-yellow: #fff7a0;
    --ice-blue: #33a6d7;
    --ice-light: #cdeef8;
    --ice-mid: #8fd0e8;
    --cola: #6b4124;
    --foam: #f2f2ee;
    --lime: #acd136;
    --ink: #1d1d1b;
    --white: #ffffff;
  }
  html, body {
    margin: 0;
    padding: 0;
    width: 1200px;
    height: 296px;
    overflow: hidden;
  }
  .header-banner {
    position: relative;
    width: 1200px;
    height: 296px;
    overflow: hidden;
    background:
      radial-gradient(ellipse 380px 160px at 65% 60%, rgba(255,255,255,0.55) 0%, rgba(255,255,255,0) 70%),
      radial-gradient(ellipse at 62% 55%, var(--pale-yellow) 0%, var(--sun-yellow) 65%);
    font-family: "Luckiest Guy", "Arial Black", Arial, sans-serif;
    font-weight: 900;
    text-transform: uppercase;
  }
  .drink-visual {
    position: absolute;
    left: 0;
    top: 0;
    width: 420px;
    height: 296px;
    background:
      linear-gradient(90deg, rgba(251,237,34,0) 80%, var(--sun-yellow) 100%),
      linear-gradient(180deg, rgba(205,238,248,0) 70%, var(--ice-mid) 100%),
      linear-gradient(135deg, var(--ice-light) 0%, var(--foam) 30%, var(--foam) 45%, var(--cola) 75%, #3b2414 100%);
  }
  .ice-corner {
    position: absolute;
    right: 0;
    top: 0;
    width: 80px;
    height: 64px;
    border-bottom-left-radius: 40px;
    background: linear-gradient(200deg, var(--ice-light), var(--ice-mid));
  }
  .ice-strip {
    position: absolute;
    right: 200px;
    bottom: 0;
    width: 80px;
    height: 26px;
    border-top-left-radius: 26px;
    border-top-right-radius: 12px;
    background: linear-gradient(180deg, var(--ice-light), var(--ice-mid));
  }
  .headline {
    position: absolute;
    left: 445px;
    top: 28px;
    margin: 0;
    font-weight: 900;
    font-size: 96px;
    line-height: 1.18;
    color: var(--ice-blue);
    text-shadow: 5px 5px 0 var(--white);
    letter-spacing: -2px;
  }
  .headline span { display: block; }
  .price {
    position: absolute;
    left: 736px;
    top: -8px;
    font-size: 300px;
    line-height: 1;
    color: var(--ice-blue);
    text-shadow: 6px 6px 0 var(--white);
    letter-spacing: -8px;
    transform: scaleX(0.86);
    transform-origin: left top;
  }
  .price-cents {
    position: absolute;
    left: 1014px;
    top: 12px;
    font-size: 96px;
    line-height: 1;
    color: var(--ice-blue);
    text-shadow: 4px 4px 0 var(--white);
  }
  .price-size {
    position: absolute;
    left: 1030px;
    top: 140px;
    font-size: 28px;
    line-height: 1.12;
    letter-spacing: -1px;
    color: var(--ice-blue);
    text-shadow: 3px 3px 0 var(--white);
  }
  .price-size span { display: block; }
  .brand-tag {
    position: absolute;
    right: 0;
    bottom: 0;
    width: 210px;
    height: 70px;
    background: var(--white);
    border-top-left-radius: 34px;
    display: flex;
    align-items: center;
    justify-content: center;
    gap: 8px;
  }
  .brand-mark {
    width: 16px;
    height: 16px;
    border-radius: 50%;
    background: var(--lime);
  }
  .brand-name {
    font-size: 38px;
    line-height: 1;
    color: var(--ink);
    text-transform: none;
  }
</style>
</head>
<body>
  <div class="header-banner">
    <div class="drink-visual" role="img" aria-label="Photo of a white foam tillstop cup tilted with cola and ice cubes splashing out, sitting in a bed of ice cubes"></div>
    <div class="ice-corner" role="img" aria-label="Photo of ice cubes in the top corner"></div>
    <div class="ice-strip" role="img" aria-label="Photo of ice cubes along the bottom edge"></div>

    <h1 class="headline"><span>Pay</span><span>Less!</span></h1>
    <div class="price">79</div>
    <div class="price-cents">¢</div>
    <div class="price-size"><span>32 oz</span><span>Fountain</span></div>

    <div class="brand-tag">
      <span class="brand-mark"></span>
      <span class="brand-name">tillstop</span>
    </div>
  </div>
</body>
</html>
```